July 4th Postcard to existing clients

5x7 postcard wishing our clients happy 4th of July. Card should read on the back "Thank You For Being A Valued Client!. Stay Safe And Enjoy Your Independence Day Celebrations!"

Patriotic theme with fireworks is ideal. We are a law firm so should still have a feel of professionalism while still being fun since it is for a fun holiday.

```html
<!DOCTYPE html>
<html lang="en">
<head>
<meta charset="utf-8">
<title>Harlow Law – 4th of July Postcard</title>
<link rel="stylesheet" href="https://fonts.googleapis.com/css2?family=Oswald:wght@700&family=Lato:wght@300;400;700;900&display=swap">
<style>
  :root {
    --navy: #14238a;
    --navy-light: #2a3db4;
    --red: #c91f26;
    --red-dark: #a8161c;
    --white: #ffffff;
    --ink: #2b2b2b;
    --grey: #5f6368;
    --line: #7a7a7a;
    --burst: #e6e8ee;
    --page: #f2f2f2;
  }
  * { box-sizing: border-box; margin: 0; padding: 0; }
  html, body { width: 1200px; height: 1200px; overflow: hidden; }
  body {
    background: var(--page);
    font-family: "Lato", Arial, sans-serif;
    display: flex; flex-direction: column; align-items: center; justify-content: center;
    gap: 34px;
  }
  .postcard {
    position: relative; width: 770px; height: 550px;
    background: var(--white); overflow: hidden;
    box-shadow: 0 6px 18px rgba(0,0,0,.18);
  }

  /* Front */
  .front-stars {
    position: absolute; left: 0; top: 0; width: 100%; height: 120px;
    background:
      radial-gradient(ellipse 160px 90px at 12% 40%, rgba(255,255,255,.22), transparent 70%),
      radial-gradient(ellipse 160px 90px at 45% 70%, rgba(255,255,255,.18), transparent 70%),
      radial-gradient(ellipse 160px 90px at 80% 35%, rgba(255,255,255,.22), transparent 70%),
      linear-gradient(180deg, var(--navy-light), var(--navy));
  }
  .front-band-red {
    position: absolute; left: 0; top: 120px; width: 100%; height: 28px;
    background: var(--red);
    border-top: 3px solid var(--white);
  }
  .front-burst {
    position: absolute; left: 0; top: 148px; width: 100%; height: 244px;
    background:
      radial-gradient(circle at 52% 55%, var(--burst) 0%, rgba(230,232,238,.5) 30%, transparent 62%),
      radial-gradient(circle at 14% 80%, rgba(230,232,238,.8) 0%, transparent 22%),
      radial-gradient(circle at 88% 40%, rgba(230,232,238,.8) 0%, transparent 20%);
  }
  .front-greeting { position: absolute; left: 0; top: 160px; width: 100%; text-align: center; }
  .greeting-happy {
    font-family: "Oswald", "Arial Narrow", sans-serif; font-weight: 700;
    font-size: 124px; line-height: 1; color: var(--navy); letter-spacing: 2px;
  }
  .greeting-day {
    font-family: "Lato", Arial, sans-serif; font-weight: 900;
    font-size: 56px; line-height: 1.1; color: var(--ink); margin-top: 4px;
  }
  .front-band-blue {
    position: absolute; left: 0; top: 392px; width: 100%; height: 28px;
    background: var(--navy);
    border-bottom: 3px solid var(--white);
  }
  .front-footer { position: absolute; left: 0; top: 420px; width: 100%; height: 130px; display: flex; }
  .firm-mark {
    width: 48%; display: flex; align-items: center; justify-content: center; gap: 12px;
  }
  .firm-mark .mark-square { width: 22px; height: 22px; background: var(--grey); }
  .firm-mark .firm-name {
    font-family: "Lato", Arial, sans-serif; font-weight: 400;
    font-size: 38px; color: var(--grey); letter-spacing: 1px;
  }
  .contact-block {
    width: 52%; background: linear-gradient(180deg, var(--red), var(--red-dark)); color: var(--white);
    padding: 0 0 0 40px;
    display: flex; flex-direction: column; justify-content: center;
  }
  .contact-main { font-weight: 900; font-size: 23px; margin-bottom: 6px; }
  .contact-row { display: flex; align-items: center; gap: 8px; font-size: 16px; font-weight: 400; line-height: 1.5; }
  .contact-row svg { width: 13px; height: 13px; fill: var(--white); flex: none; }

  /* Back */
  .back-burst {
    position: absolute; inset: 0;
    background:
      radial-gradient(circle at 62% 62%, var(--burst) 0%, transparent 40%),
      radial-gradient(circle at 70% 18%, rgba(230,232,238,.8) 0%, transparent 18%);
  }
  .back-photo {
    position: absolute; left: 0; top: 0; width: 440px; height: 200px;
    background: linear-gradient(120deg, #3c4a86 0%, #8a5a3a 40%, #b07a48 65%, #d7b77a 100%);
  }
  .back-rule { position: absolute; left: 0; top: 200px; width: 440px; height: 6px; background: var(--red); }
  .address-lines { position: absolute; right: 40px; top: 60px; width: 230px; }
  .address-lines span { display: block; height: 1px; background: var(--line); margin-bottom: 48px; }
  .back-message { position: absolute; left: 40px; top: 226px; }
  .msg-thanks { font-weight: 900; font-size: 62px; line-height: 1; color: var(--ink); }
  .msg-line { font-weight: 300; font-size: 26px; line-height: 1.2; color: var(--ink); }
  .msg-line:first-of-type { margin-top: 8px; }
  .msg-holiday { font-weight: 700; font-size: 34px; line-height: 1.2; color: var(--red); margin-top: 4px; }
  .msg-celebrate { font-weight: 900; font-size: 56px; line-height: 1; color: var(--red); }
  .back-stripe { position: absolute; left: 0; bottom: 0; width: 100%; height: 22px; background: var(--red); }
</style>
</head>
<body>

<section class="postcard postcard-front">
  <div class="front-stars" role="img" aria-label="White stars on a navy blue field"></div>
  <div class="front-band-red"></div>
  <div class="front-burst" role="img" aria-label="Faint grey fireworks bursting behind the greeting"></div>
  <div class="front-greeting">
    <div class="greeting-happy">HAPPY</div>
    <div class="greeting-day">4th of July</div>
  </div>
  <div class="front-band-blue"></div>
  <div class="front-footer">
    <div class="firm-mark">
      <span class="mark-square"></span>
      <span class="firm-name">HARLOW LAW</span>
    </div>
    <div class="contact-block">
      <div class="contact-main">1-800-555-0142</div>
      <div class="contact-row">
        <svg viewBox="0 0 24 24"><path d="M6.6 10.8a15.1 15.1 0 0 0 6.6 6.6l2.2-2.2a1 1 0 0 1 1-.25 11.4 11.4 0 0 0 3.6.57 1 1 0 0 1 1 1V20a1 1 0 0 1-1 1A17 17 0 0 1 3 4a1 1 0 0 1 1-1h3.5a1 1 0 0 1 1 1c0 1.25.2 2.45.57 3.57a1 1 0 0 1-.25 1z"/></svg>
        (555) 010-2233
      </div>
      <div class="contact-row">
        <svg viewBox="0 0 24 24"><path d="M6 2h12v6H6zM4 9h16a2 2 0 0 1 2 2v7h-4v4H6v-4H2v-7a2 2 0 0 1 2-2zm4 7v4h8v-4z"/></svg>
        (555) 010-4477
      </div>
      <div class="contact-row">
        <svg viewBox="0 0 24 24"><path d="M12 2a7 7 0 0 0-7 7c0 5.2 7 13 7 13s7-7.8 7-13a7 7 0 0 0-7-7zm0 9.5A2.5 2.5 0 1 1 12 6.5a2.5 2.5 0 0 1 0 5z"/></svg>
        1820 West Maple Avenue
      </div>
    </div>
  </div>
</section>

<section class="postcard postcard-back">
  <div class="back-burst" role="img" aria-label="Faint grey fireworks across the card background"></div>
  <div class="back-photo" role="img" aria-label="Photo of a wooden gavel and brass scales of justice before an American flag"></div>
  <div class="back-rule"></div>
  <div class="address-lines"><span></span><span></span><span></span></div>
  <div class="back-message">
    <div class="msg-thanks">Thank You</div>
    <div class="msg-line">For Being A Valued Client</div>
    <div class="msg-line">Stay Safe And Enjoy Your</div>
    <div class="msg-holiday">Independence Day</div>
    <div class="msg-celebrate">Celebrations</div>
  </div>
  <div class="back-stripe"></div>
</section>

</body>
</html>
```